Flyer for family counseling

For my family counseling I'm looking for a design for flyers. Important is not only the appearance of the flyer, but also the content design. All important contents can be found on my website: www.brigitte-volkanter.at The following items should NOT appear on the flyer: - constellation work - bereavement and palliative work My logo should definitely be on the flyer. Source files are available.

Target Market(s)

Families, individuals, children, couples in need of psychological support.

Colors

Designer to choose colors to be used in the design.

Requirements
Must have
• My logo - source files available Website and contact data Recognition value from website to flyer and vice versa
Should not have
• Mention of the constellation work and mourning and palliative work not desired.

```html
<!DOCTYPE html>
<html lang="de">
<head>
<meta charset="utf-8">
<title>Familienberatung Stadlau – Flyer</title>
<link rel="stylesheet" href="https://fonts.googleapis.com/css2?family=Lato:ital,wght@0,400;0,700;0,900;1,400&family=PT+Sans+Narrow:wght@400&display=swap">
<style>
  :root {
    --teal-dark: #1aa79d;
    --teal-light: #2fd5c5;
    --teal-text: #1fa59c;
    --logo-blue: #1d4f9c;
    --ink: #333333;
    --white: #ffffff;
  }
  * { margin: 0; padding: 0; box-sizing: border-box; }
  html, body { width: 859px; height: 1200px; overflow: hidden; background: var(--white); }
  .flyer { position: relative; width: 859px; height: 1200px; font-family: "Lato", sans-serif; color: var(--ink); background: var(--white); }

  .brand { position: absolute; left: 40px; top: 96px; display: flex; align-items: center; gap: 10px; }
  .brand-dot { width: 14px; height: 14px; border-radius: 50%; background: var(--teal-dark); }
  .brand-name { font-weight: 700; font-size: 15px; letter-spacing: 1.5px; color: var(--logo-blue); text-transform: uppercase; }

  .block { position: absolute; }
  .block.dark { background: var(--teal-dark); }
  .block.light { background: var(--teal-light); }

  .web-band { position: absolute; left: 485px; top: 53px; width: 374px; height: 50px; background: var(--teal-light); color: var(--white); font-size: 27px; display: flex; align-items: center; padding-left: 25px; }

  .hero {
    position: absolute; left: 0; top: 143px; width: 859px; height: 499px;
    background:
      radial-gradient(ellipse 90px 170px at 235px 360px, rgba(240,90,60,0.85), rgba(240,90,60,0) 100%),
      radial-gradient(ellipse 150px 160px at 160px 330px, rgba(250,246,240,0.95), rgba(250,246,240,0) 100%),
      radial-gradient(ellipse 120px 110px at 230px 150px, rgba(228,196,130,0.9), rgba(228,196,130,0) 100%),
      radial-gradient(ellipse 130px 190px at 420px 300px, rgba(150,210,80,0.9), rgba(150,210,80,0) 100%),
      radial-gradient(ellipse 100px 110px at 450px 120px, rgba(214,180,120,0.85), rgba(214,180,120,0) 100%),
      radial-gradient(ellipse 70px 140px at 570px 370px, rgba(250,250,250,0.95), rgba(250,250,250,0) 100%),
      radial-gradient(ellipse 150px 210px at 760px 380px, rgba(232,190,200,0.95), rgba(232,190,200,0) 100%),
      radial-gradient(ellipse 110px 120px at 730px 170px, rgba(200,150,100,0.85), rgba(200,150,100,0) 100%),
      radial-gradient(ellipse 100px 40px at 320px 40px, rgba(120,170,70,0.6), rgba(120,170,70,0) 100%),
      linear-gradient(180deg, #f1ece6 0%, #ece3d8 70%, #e4d6c3 100%);
  }

  .hero-title { position: absolute; left: 0; top: 543px; width: 353px; height: 71px; background: var(--teal-light); color: var(--white); font-size: 28px; display: flex; align-items: center; padding-left: 19px; }

  .service { position: absolute; width: 400px; }
  .service-photo { position: absolute; left: 0; top: 0; width: 159px; height: 112px; border-radius: 0 0 16px 0; }
  .service-title { position: absolute; left: 174px; font-size: 16px; font-weight: 400; color: var(--teal-text); }
  .service-text { position: absolute; left: 174px; width: 190px; font-family: "PT Sans Narrow", sans-serif; font-size: 9.2px; line-height: 12.4px; color: #222; text-align: justify; }

  .voices { position: absolute; left: 0; top: 929px; width: 859px; height: 201px; background: var(--teal-dark); }
  .voices-heading { position: absolute; left: 45px; top: 18px; font-size: 26px; font-weight: 400; color: var(--white); }
  .quote { position: absolute; top: 63px; height: 115px; background: var(--white); padding: 19px 12px 0 12px; }
  .quote-text { font-style: italic; font-size: 13px; line-height: 16px; color: #444; text-align: justify; }
  .quote-author { position: absolute; right: 22px; bottom: 10px; font-size: 13px; color: #222; }
  .quote-mark { position: absolute; font-weight: 900; font-size: 80px; line-height: 1; color: var(--teal-light); }

  .footer { position: absolute; left: 0; top: 1130px; width: 859px; height: 70px; background: var(--teal-light); color: var(--white); font-size: 14.5px; display: flex; align-items: center; justify-content: center; }
</style>
</head>
<body>
<div class="flyer">

  <header>
    <div class="brand">
      <span class="brand-dot"></span>
      <span class="brand-name">Brigitte Volkanter</span>
    </div>
    <div class="block dark" style="left:395px; top:53px; width:33px; height:50px;"></div>
    <div class="block light" style="left:441px; top:53px; width:33px; height:50px;"></div>
    <div class="web-band">www.brigitte-volkanter.at</div>
  </header>

  <div class="hero" role="img" aria-label="Foto: Beraterin lacht mit zwei Mädchen am Spieltisch mit Holzfiguren, bemalten Schachteln und Buntstiften"></div>
  <div class="hero-title">Familienberatung Stadlau</div>
  <div class="block light" style="left:360px; top:543px; width:58px; height:71px;"></div>
  <div class="block dark" style="left:430px; top:543px; width:58px; height:71px;"></div>

  <section class="services">
    <article class="service" style="left:45px; top:661px;">
      <div class="service-photo" role="img" aria-label="Foto: Einzelgespräch im Beratungsraum mit Sesseln" style="background:radial-gradient(ellipse 30px 40px at 75px 50px, rgba(190,40,40,0.7), rgba(190,40,40,0)), radial-gradient(ellipse 40px 25px at 50px 90px, rgba(50,50,50,0.7), rgba(50,50,50,0)), radial-gradient(ellipse 30px 40px at 140px 40px, rgba(110,150,60,0.7), rgba(110,150,60,0)), linear-gradient(180deg,#eee8de 0%,#e2d7c6 55%,#c08a52 75%,#a86a36 100%);"></div>
      <h3 class="service-title" style="top:16px;">Einzelberatung</h3>
      <p class="service-text" style="top:40px;">Für den ganz persönlichen Weg zur Selbstbestimmung. Ist er einmal betreten, wird die persönliche Entwicklung ein wundervolles Abenteuer.</p>
    </article>

    <article class="service" style="left:443px; top:661px;">
      <div class="service-photo" role="img" aria-label="Foto: Paargespräch im Beratungsraum" style="background:radial-gradient(ellipse 45px 25px at 40px 75px, rgba(40,40,40,0.75), rgba(40,40,40,0)), radial-gradient(ellipse 40px 25px at 110px 78px, rgba(50,50,60,0.7), rgba(50,50,60,0)), radial-gradient(ellipse 30px 30px at 65px 20px, rgba(250,240,220,0.9), rgba(250,240,220,0)), linear-gradient(180deg,#f1ebe1 0%,#e6dccd 55%,#c58f58 78%,#a66a38 100%);"></div>
      <h3 class="service-title" style="left:184px; top:16px;">Paarberatung</h3>
      <p class="service-text" style="left:184px; top:42px;">Muster können aufgelöst werden! Gerne unterstütze ich Sie auf Ihrem Weg, sich in Ihrer Partnerschaft wieder auf deren Grundlage zu besinnen. Darauf aufzubauen, einen viel versprechenden Neubeginn zu wagen.</p>
    </article>

    <article class="service" style="left:45px; top:795px;">
      <div class="service-photo" role="img" aria-label="Foto: Familie mit Kindern in einem Raum mit Kleiderständer" style="background:radial-gradient(ellipse 45px 40px at 75px 75px, rgba(200,60,60,0.8), rgba(200,60,60,0)), radial-gradient(ellipse 40px 30px at 115px 55px, rgba(160,70,120,0.6), rgba(160,70,120,0)), radial-gradient(ellipse 25px 45px at 30px 50px, rgba(60,70,90,0.6), rgba(60,70,90,0)), linear-gradient(180deg,#d9d4cc 0%,#c8b9a6 50%,#8a6b55 100%);"></div>
      <h3 class="service-title" style="top:6px;">Erziehungsberatung</h3>
      <p class="service-text" style="top:30px;">Meine Aufgabe besteht darin, Sie in einem vertrauensvollen Rahmen zu unterstützen, eine neue Form der elterlichen Kooperation zu finden und Ihren Blick und Ihre Aufmerksamkeit auf die Bedürfnisse und Nöte der Kinder/des Kindes zu richten, förderliche Haltungen bzw. Verhaltensweisen zu erarbeiten damit Kinder entlastet und ihre Entwicklungsbedürfnisse wieder wahrgenommen werden.</p>
    </article>

    <article class="service" style="left:443px; top:795px;">
      <div class="service-photo" role="img" aria-label="Foto: Mutter liest mit zwei Töchtern ein Buch" style="background:radial-gradient(ellipse 50px 30px at 90px 20px, rgba(120,170,70,0.85), rgba(120,170,70,0)), radial-gradient(ellipse 30px 25px at 75px 85px, rgba(200,60,70,0.7), rgba(200,60,70,0)), radial-gradient(ellipse 30px 40px at 130px 75px, rgba(120,50,70,0.7), rgba(120,50,70,0)), radial-gradient(ellipse 30px 40px at 30px 70px, rgba(90,100,80,0.6), rgba(90,100,80,0)), linear-gradient(180deg,#dfe6d2 0%,#e6d8c6 50%,#b8a08c 100%);"></div>
      <h3 class="service-title" style="left:184px; top:6px;">Familie &amp; Kinder</h3>
      <p class="service-text" style="left:184px; top:30px;">Das Ziel einer Familientherapie ist, eine positive Beziehungsveränderung zwischen den einzelnen Familienmitgliedern zu erreichen. Respekt, gegenseitiges Verständnis und Einfühlungsvermögen füreinander sind wesentlich für ein funktionierendes Zusammenleben in einer Familie. Diese Werte können in einer Familienberatung wieder in den Mittelpunkt gerückt beziehungsweise verbessert werden.</p>
    </article>
  </section>

  <section class="voices">
    <h2 class="voices-heading">Stimmen von Klienten</h2>

    <blockquote class="quote" style="left:46px; width:360px;">
      <p class="quote-text">Brigitte Volkanter zeichnet sich durch Wärme, Souveränität, Ruhe und Sorgfältigkeit aus. Sicher und liebevoll begleitet sie durch den Prozess. Sie ist neutral, aber interessiert. Man fühlt sich gut aufgehoben, auch wenn es "ans Eingemachte" geht.</p>
      <span class="quote-author">Frau R. Klientin</span>
    </blockquote>
    <div class="quote-mark" style="left:22px; top:46px;">“</div>
    <div class="quote-mark" style="left:382px; top:148px;">”</div>

    <blockquote class="quote" style="left:453px; width:351px; padding:26px 22px 0 22px;">
      <p class="quote-text">Mein Weg war voller Steine und Holz. Ich nahm den Besen in die Hand und kehrte. Frau Volkanter begleitete mich dabei.</p>
      <span class="quote-author">Frau H. Klientin</span>
    </blockquote>
    <div class="quote-mark" style="left:430px; top:46px;">“</div>
    <div class="quote-mark" style="left:782px; top:148px;">”</div>
  </section>

  <footer class="footer">Lindenhofgasse 14/3, 1220 Vienna | familienberatung@brigitte-volkanter.at | Telephone: +43 660 418 27 95</footer>

</div>
</body>
</html>
```